Business Card for Orvane Parts Wholesale supplier

Hi There! I need a new business card for our company. We are specialized in selling Orvane parts, mostly we sell new LCD screens for Telvox and Slatrons. I would like to see that back in the design.

You can find the colors and logo's on our website: www.dorvak-example.nl

Industry/Entity Type

Business

Contact Information for Business Card

My Details:
Lars Vintorp

Phone: 0031612873406
E-mail: Lars@dorvak-example.nl

Slogan: "Because Quality Matters"

Font styles to use
Sans Serif

Colors

Designer to choose colors to be used in the design.

Requirements
Must have
• A Black backside with the Dorvak logo on it. The front side should be clean with only my contact details.
• But I'm also open for something really different or awesome!
Nice to have
• Remember that we are in the parts & repairing industry, So i'll be handing those business cards mainly to repair companies. Maybe you can do something with that thought :)

```html
<!DOCTYPE html>
<html lang="en">
<head>
<meta charset="utf-8">
<title>Dorvak Business Card</title>
<link rel="stylesheet" href="https://fonts.googleapis.com/css2?family=Arimo:wght@400;700&display=swap">
<style>
  :root {
    --backdrop: #d9d9d9;
    --card: #231f20;
    --card-edge: #151314;
    --accent: #e8671e;
    --ink-light: #f2f2f2;
    --ink-soft: #d6d6d6;
  }
  * { margin: 0; padding: 0; box-sizing: border-box; }
  html, body {
    width: 1200px;
    height: 1200px;
    overflow: hidden;
    background: var(--backdrop);
    font-family: "Arimo", Arial, sans-serif;
  }
  .sheet {
    position: relative;
    width: 1200px;
    height: 1200px;
  }
  .card {
    position: absolute;
    left: 220px;
    width: 760px;
    height: 434px;
    background: var(--card);
    box-shadow: 0 3px 0 var(--card-edge), 0 10px 24px rgba(0,0,0,0.25);
  }
  .card--back { top: 100px; }
  .card--front { top: 640px; }

  .brand {
    display: flex;
    align-items: center;
    gap: 18px;
  }
  .brand__mark {
    width: 52px;
    height: 52px;
    background: var(--accent);
  }
  .brand__name {
    color: var(--ink-light);
    font-weight: 700;
    font-size: 64px;
    letter-spacing: 1px;
    line-height: 1;
  }
  .card--back .brand {
    position: absolute;
    left: 50%;
    top: 50%;
    transform: translate(-50%, -50%);
  }

  .card--front .brand {
    position: absolute;
    left: 60px;
    top: 88px;
  }
  .card--front .brand__mark { width: 58px; height: 58px; }
  .card--front .brand__name { font-size: 70px; }

  .holder {
    position: absolute;
    left: 60px;
    top: 206px;
    color: var(--accent);
    font-weight: 700;
    font-size: 28px;
    letter-spacing: 0.5px;
  }
  .divider {
    position: absolute;
    left: 330px;
    right: 0;
    top: 226px;
    height: 1px;
    background: var(--accent);
  }
  .slogan {
    position: absolute;
    right: 40px;
    top: 250px;
    color: var(--ink-soft);
    font-size: 19px;
  }
  .contacts {
    position: absolute;
    left: 60px;
    top: 262px;
    list-style: none;
  }
  .contacts__item {
    display: flex;
    align-items: center;
    gap: 10px;
    color: var(--ink-light);
    font-size: 22px;
    margin-bottom: 12px;
  }
  .contacts__icon {
    width: 18px;
    height: 18px;
    flex: none;
  }
</style>
</head>
<body>
<main class="sheet">

  <section class="card card--back" aria-label="Card back">
    <div class="brand">
      <span class="brand__mark"></span>
      <span class="brand__name">dorvak</span>
    </div>
  </section>

  <section class="card card--front" aria-label="Card front">
    <div class="brand">
      <span class="brand__mark"></span>
      <span class="brand__name">dorvak</span>
    </div>

    <p class="holder">LARS VINTORP</p>
    <div class="divider"></div>
    <p class="slogan">Because Quality Matters</p>

    <ul class="contacts">
      <li class="contacts__item">
        <svg class="contacts__icon" viewBox="0 0 18 18" aria-hidden="true">
          <rect width="18" height="18" fill="#e8671e"/>
          <path d="M5 4.5 L7 4.5 L8 7 L6.8 8 Q8 10.5 10 11.2 L11 10 L13.5 11 L13.5 13 Q12.5 14 11 13.6 Q6 12 4.4 7 Q4.2 5.4 5 4.5 Z" fill="#231f20"/>
        </svg>
        <span>0031612873406</span>
      </li>
      <li class="contacts__item">
        <svg class="contacts__icon" viewBox="0 0 18 18" aria-hidden="true">
          <rect width="18" height="18" fill="#e8671e"/>
          <rect x="3.5" y="5" width="11" height="8" fill="none" stroke="#231f20" stroke-width="1.4"/>
          <path d="M3.5 5 L9 9.5 L14.5 5" fill="none" stroke="#231f20" stroke-width="1.4"/>
        </svg>
        <span>Lars@dorvak-example.nl</span>
      </li>
      <li class="contacts__item">
        <svg class="contacts__icon" viewBox="0 0 18 18" aria-hidden="true">
          <rect width="18" height="18" fill="#e8671e"/>
          <circle cx="9" cy="9" r="5" fill="none" stroke="#231f20" stroke-width="1.3"/>
          <ellipse cx="9" cy="9" rx="2.2" ry="5" fill="none" stroke="#231f20" stroke-width="1.1"/>
          <line x1="4" y1="9" x2="14" y2="9" stroke="#231f20" stroke-width="1.1"/>
        </svg>
        <span>www.dorvak-example.nl</span>
      </li>
    </ul>
  </section>

</main>
</body>
</html>
```